Redesign our iOS App Design mockups

- Redesign our current Zelvo App Mockup
- Keep the design simple so that programmers do not have to do too much extra work to make your design work.
- Look at the attached website screenshot for the overall look and feel, and color scheme
- Convert the attached vector logo to iOS Icon format.
- Deliver all graphics in the density required for Zelvo QT Grand.
- I have attached the current iOS mockup in a .ZIP file but you can view it here as well: https://boards.kelmoraview.com/share/TRWQBN8HDK2

Target Market(s)

Mostly Male Internet Consumers between the ages of 20 and 35

Industry/Entity Type

Internet

Colors

Designer to choose colors to be used in the design.

Requirements
Must have
• - Deliver all graphics in the density required for Zelvo QT Grand
• - Should also look good on Murel and Murel pro
• - Design type should be “FLAT.”
• - Spell out fonts used in the design and where they are used. Also, include font sizes.
• - Please use ALL the elements in each page and use all placements and text EXACTLY. Please do not improvise with text or components.
• I have designed the mockup exactly the way I like it. I just want it to made to look better.
Should not have

```html
<!DOCTYPE html>
<html lang="en">
<head>
<meta charset="utf-8">
<title>Settings</title>
<link rel="stylesheet" href="https://fonts.googleapis.com/css2?family=Montserrat:wght@300;400;500;600&display=swap">
<style>
  :root {
    --page-bg: #000000;
    --header-start: #dc4436;
    --header-end: #f6604f;
    --header-text: #ffffff;
    --title-text: #151515;
    --screen-bg: #efeef4;
    --cell-bg: #ffffff;
    --cell-line: #e3e3e8;
    --text-main: #1a1a1a;
    --text-sub: #555860;
    --text-section: #4a4a4f;
    --text-footer: #8c8c92;
    --chevron: #b9b9be;
    --toggle-on: #4cd964;
    --indicator: #111111;
  }
  * { box-sizing: border-box; margin: 0; padding: 0; }
  html, body {
    width: 1200px; height: 1200px; overflow: hidden;
    background: var(--page-bg);
    font-family: "Montserrat", Arial, sans-serif;
  }
  .screen {
    position: absolute; left: 332px; top: 20px;
    width: 564px; height: 1220px;
    transform: scale(0.95); transform-origin: top left;
    background: var(--screen-bg);
    border-radius: 44px; overflow: hidden;
  }
  .nav-bar {
    position: absolute; left: 0; top: 0; width: 564px; height: 136px;
    background: linear-gradient(100deg, var(--header-start) 0%, var(--header-start) 40%, var(--header-end) 100%);
  }
  .status-time {
    position: absolute; left: 43px; top: 19px;
    font-size: 20px; font-weight: 600; color: var(--title-text);
  }
  .status-icons { position: absolute; right: 18px; top: 22px; }
  .nav-back {
    position: absolute; left: 16px; top: 84px;
    display: flex; align-items: center; gap: 14px;
    color: var(--header-text); font-size: 22px; font-weight: 500;
  }
  .nav-title {
    position: absolute; left: 0; right: 0; top: 78px; text-align: center;
    font-size: 27px; font-weight: 500; color: var(--title-text);
  }
  .section-label {
    position: absolute; left: 17px; top: 197px;
    font-size: 21px; font-weight: 300; color: var(--text-section);
  }
  .group {
    position: absolute; left: 0; width: 564px; background: var(--cell-bg);
    border-top: 1px solid var(--cell-line); border-bottom: 1px solid var(--cell-line);
  }
  .group-app { top: 230px; }
  .group-legal { top: 491px; }
  .cell { position: relative; height: 60px; }
  .cell + .cell::before {
    content: ""; position: absolute; left: 17px; right: 0; top: 0;
    border-top: 1px solid var(--cell-line);
  }
  .cell-toggle { height: 115px; }
  .toggle-title {
    position: absolute; left: 17px; top: 14px;
    font-size: 24px; font-weight: 500; color: var(--text-main);
  }
  .toggle-desc {
    position: absolute; left: 17px; top: 48px; width: 340px;
    font-size: 17px; line-height: 24px; color: var(--text-sub);
  }
  .switch {
    position: absolute; left: 474px; top: 37px;
    width: 72px; height: 41px; border-radius: 21px; background: var(--toggle-on);
  }
  .switch-knob {
    position: absolute; right: 2px; top: 2px; width: 37px; height: 37px;
    border-radius: 50%; background: #fff; box-shadow: 0 2px 4px rgba(0,0,0,.2);
  }
  .cell-icon { position: absolute; left: 26px; top: 13px; width: 34px; height: 34px; }
  .cell-label {
    position: absolute; left: 84px; top: 14px;
    font-size: 24px; font-weight: 500; color: var(--text-main);
  }
  .chevron { position: absolute; right: 18px; top: 19px; }
  .app-version {
    position: absolute; left: 0; right: 0; top: 1123px; text-align: center;
    font-size: 21px; font-weight: 300; color: var(--text-footer);
  }
  .home-indicator {
    position: absolute; left: 162px; top: 1190px; width: 241px; height: 5px;
    border-radius: 3px; background: var(--indicator);
  }
</style>
</head>
<body>
<main class="screen">
  <header class="nav-bar">
    <span class="status-time">9:41</span>
    <svg class="status-icons" width="92" height="18" viewBox="0 0 92 18" aria-hidden="true">
      <g fill="#151515">
        <rect x="0" y="11" width="4" height="6" rx="1"/>
        <rect x="6" y="8" width="4" height="9" rx="1"/>
        <rect x="12" y="5" width="4" height="12" rx="1"/>
        <rect x="18" y="1" width="4" height="16" rx="1"/>
        <path d="M41 17 l-3.5-4 a5 5 0 0 1 7 0z"/>
        <path d="M32 8.5 a13 13 0 0 1 18 0 l-2.2 2.4 a10 10 0 0 0 -13.6 0z"/>
        <path d="M28.5 5 a18 18 0 0 1 25 0 l-2 2.2 a15 15 0 0 0 -21 0z"/>
        <rect x="59" y="2" width="28" height="14" rx="4" fill="none" stroke="#151515" stroke-width="1.6"/>
        <rect x="61.5" y="4.5" width="23" height="9" rx="2"/>
        <rect x="88.5" y="6.5" width="2" height="5" rx="1"/>
      </g>
    </svg>
    <div class="nav-back">
      <svg width="14" height="24" viewBox="0 0 14 24" aria-hidden="true"><path d="M12 2 L3 12 L12 22" fill="none" stroke="#fff" stroke-width="3" stroke-linecap="round" stroke-linejoin="round"/></svg>
      <span>Home</span>
    </div>
    <h1 class="nav-title">Settings</h1>
  </header>

  <p class="section-label">APP SETTINGS</p>

  <section class="group group-app">
    <div class="cell cell-toggle">
      <span class="toggle-title">Kill Switch</span>
      <span class="toggle-desc">Cuts Internet connectivity when your VPN connection gets lost</span>
      <span class="switch"><span class="switch-knob"></span></span>
    </div>
    <div class="cell">
      <svg class="cell-icon" viewBox="0 0 34 34" aria-hidden="true">
        <path d="M17 2 L30 7 V16 C30 24 24 30 17 33 C10 30 4 24 4 16 V7 Z" fill="#111"/>
        <path d="M11.5 17 L15.5 21 L22.5 13" fill="none" stroke="#fff" stroke-width="2.6" stroke-linecap="round" stroke-linejoin="round"/>
      </svg>
      <span class="cell-label">Protocols</span>
      <svg class="chevron" width="14" height="24" viewBox="0 0 14 24" aria-hidden="true"><path d="M2 2 L12 12 L2 22" fill="none" stroke="var(--chevron)" stroke-width="2.4" stroke-linecap="round" stroke-linejoin="round"/></svg>
    </div>
    <div class="cell">
      <svg class="cell-icon" viewBox="0 0 34 34" aria-hidden="true">
        <path d="M10 8 A12 12 0 1 0 24 8" fill="none" stroke="#111" stroke-width="3.6" stroke-linecap="round"/>
        <line x1="17" y1="3" x2="17" y2="16" stroke="#111" stroke-width="3.6" stroke-linecap="round"/>
      </svg>
      <span class="cell-label">Logout</span>
      <svg class="chevron" width="14" height="24" viewBox="0 0 14 24" aria-hidden="true"><path d="M2 2 L12 12 L2 22" fill="none" stroke="var(--chevron)" stroke-width="2.4" stroke-linecap="round" stroke-linejoin="round"/></svg>
    </div>
  </section>

  <section class="group group-legal">
    <div class="cell">
      <svg class="cell-icon" viewBox="0 0 34 34" aria-hidden="true">
        <g fill="none" stroke="#111" stroke-width="2" stroke-linejoin="round" stroke-linecap="round">
          <path d="M10 4 H29 L25 28 C24.5 31 22 32 19 32 H6 C4 32 3 30 4 28 L5 26 H8 Z"/>
          <path d="M8 26 H21 C21 29 20 31 19 32"/>
          <line x1="13" y1="10" x2="24" y2="10"/>
          <line x1="12" y1="14" x2="23" y2="14"/>
          <line x1="11" y1="18" x2="22" y2="18"/>
          <line x1="10.5" y1="22" x2="18" y2="22"/>
        </g>
      </svg>
      <span class="cell-label">Terms of Service</span>
      <svg class="chevron" width="14" height="24" viewBox="0 0 14 24" aria-hidden="true"><path d="M2 2 L12 12 L2 22" fill="none" stroke="var(--chevron)" stroke-width="2.4" stroke-linecap="round" stroke-linejoin="round"/></svg>
    </div>
    <div class="cell">
      <svg class="cell-icon" viewBox="0 0 34 34" aria-hidden="true">
        <path d="M5 3 H18 L24 9 V17" fill="none" stroke="#111" stroke-width="2" stroke-linejoin="round"/>
        <path d="M5 3 V31 H17" fill="none" stroke="#111" stroke-width="2" stroke-linejoin="round"/>
        <path d="M18 3 V9 H24" fill="none" stroke="#111" stroke-width="2" stroke-linejoin="round"/>
        <circle cx="12" cy="15" r="3" fill="#111"/>
        <path d="M7 25 C7 20 17 20 17 25 Z" fill="#111"/>
        <circle cx="24.5" cy="25.5" r="7.5" fill="#fff" stroke="#111" stroke-width="2"/>
        <rect x="21" y="25" width="7" height="5" rx="1" fill="#111"/>
        <path d="M22.5 25 V23 a2 2 0 0 1 4 0 V25" fill="none" stroke="#111" stroke-width="1.6"/>
      </svg>
      <span class="cell-label">Privacy Policy</span>
      <svg class="chevron" width="14" height="24" viewBox="0 0 14 24" aria-hidden="true"><path d="M2 2 L12 12 L2 22" fill="none" stroke="var(--chevron)" stroke-width="2.4" stroke-linecap="round" stroke-linejoin="round"/></svg>
    </div>
  </section>

  <p class="app-version">App Version v1.1</p>
  <div class="home-indicator"></div>
</main>
</body>
</html>
```